QRV Stationery Design Project

Dear Designers,
We need a new stationery design for company to match our new logo.
Designers should provide a design for the following:
1. Business Card: 3.5x2 Inches.
2. Letterhead: A4 size.
3. Envelops: 25x35.5 Cm.
You can keep the Arabic name at the bottom of the logo Or you can use the separate attached Arabic Name.
Please refer to the attached logo guide for design information.
Sample Business Card information:
Name: Tariq Nawaf
Position: Operation Manager
Tel: +966 920007714 Ex. 500
Fax: +966 (3)8842617
Mob: +966 (5)00387251
email: tariq@qrv-example.com.sa
URL: www.qrv-example.com.sa
Address:
Al Wadi Tower, Suite 303
Nasser bin Salem Str.
Khobar, 31847
Saudi Arabia
Updates
Dear All,
Please note, we had uploaded our logo along with Arabic writing in Adobe illustrator format (.ai).
Regards,
Khalid
Dear All,
A sample data for the business card had been added as per your request.
Regards,
Khalid

```html
<!DOCTYPE html>
<html lang="en">
<head>
<meta charset="utf-8">
<title>QRV Business Card</title>
<link href="https://fonts.googleapis.com/css2?family=Titillium+Web:wght@400;600;700&display=swap" rel="stylesheet">
<style>
  :root {
    --navy: #132f55;
    --ink: #1d3a63;
    --grey-text: #4a4f57;
    --card-border: #9a9a9a;
    --page: #ffffff;
    --white: #ffffff;
  }
  * { margin: 0; padding: 0; box-sizing: border-box; }
  html, body {
    width: 1200px;
    height: 375px;
    overflow: hidden;
    background: var(--page);
    font-family: "Titillium Web", Arial, sans-serif;
  }
  .sheet { position: relative; width: 1200px; height: 375px; }

  .card-back {
    position: absolute;
    left: 25px; top: 25px;
    width: 572px; height: 325px;
    background: var(--navy);
    display: flex;
    align-items: center;
    justify-content: center;
    gap: 18px;
  }
  .card-back .brand-dot {
    width: 26px; height: 26px;
    border-radius: 50%;
    background: var(--white);
  }
  .card-back .brand-name {
    color: var(--white);
    font-size: 76px;
    font-weight: 700;
    letter-spacing: 4px;
    line-height: 1;
  }

  .card-front {
    position: absolute;
    left: 607px; top: 25px;
    width: 569px; height: 325px;
    background: var(--white);
    border: 1px solid var(--card-border);
  }
  .holder { position: absolute; left: 23px; top: 44px; }
  .holder-name {
    color: var(--ink);
    font-size: 21px;
    font-weight: 400;
    line-height: 1.2;
  }
  .holder-role {
    color: var(--grey-text);
    font-size: 16.5px;
    line-height: 1.2;
    margin-top: 4px;
  }

  .front-brand {
    position: absolute;
    right: 28px; top: 40px;
    width: 206px;
    display: flex;
    align-items: center;
    justify-content: center;
    gap: 12px;
  }
  .front-brand .brand-dot {
    width: 14px; height: 14px;
    border-radius: 50%;
    background: var(--navy);
  }
  .front-brand .brand-name {
    color: var(--navy);
    font-size: 46px;
    font-weight: 700;
    letter-spacing: 3px;
    line-height: 1;
  }

  .address { position: absolute; left: 24px; top: 170px; width: 210px; }
  .address-label {
    color: var(--ink);
    font-size: 14.5px;
    line-height: 1.2;
    padding-bottom: 3px;
    border-bottom: 1.5px solid var(--navy);
  }
  .address-lines {
    font-style: normal;
    color: var(--grey-text);
    font-size: 17px;
    line-height: 21.5px;
    margin-top: 7px;
    white-space: nowrap;
  }

  .contacts {
    position: absolute;
    left: 339px; top: 182px;
    list-style: none;
  }
  .contacts li {
    display: flex;
    align-items: center;
    height: 25.5px;
    color: var(--grey-text);
    font-size: 14px;
    white-space: nowrap;
  }
  .contacts svg {
    width: 16px; height: 16px;
    margin-right: 17px;
    flex: none;
    fill: var(--navy);
    stroke: var(--navy);
  }
</style>
</head>
<body>
<div class="sheet">

  <section class="card-back">
    <span class="brand-dot"></span>
    <span class="brand-name">QRV</span>
  </section>

  <section class="card-front">
    <div class="holder">
      <h1 class="holder-name">Tariq Nawaf</h1>
      <p class="holder-role">Operation Manager</p>
    </div>

    <div class="front-brand">
      <span class="brand-name">QRV</span>
      <span class="brand-dot"></span>
    </div>

    <div class="address">
      <h2 class="address-label">Address</h2>
      <address class="address-lines">
        Al Wadi Tower, Suite 303<br>
        Nasser bin Salem Str.<br>
        Khobar, 31847<br>
        Saudi Arabia
      </address>
    </div>

    <ul class="contacts">
      <li>
        <svg viewBox="0 0 16 16" aria-hidden="true"><path stroke="none" d="M1 5c0-2 3-3 7-3s7 1 7 3v1.5h-3.5V5h-7v1.5H1z"/><rect stroke="none" x="3" y="7" width="10" height="7" rx="1"/><circle cx="8" cy="10.5" r="1.8" fill="#fff" stroke="none"/></svg>
        +966 920007714 Ex. 500
      </li>
      <li>
        <svg viewBox="0 0 16 16" aria-hidden="true"><rect stroke="none" x="4" y="3" width="8" height="13" rx="1.2"/><rect stroke="none" x="5" y="0" width="1.5" height="3"/><rect x="5.5" y="4.5" width="5" height="3.5" fill="#fff" stroke="none"/><g fill="#fff" stroke="none"><rect x="5.5" y="9.5" width="1.3" height="1.3"/><rect x="7.4" y="9.5" width="1.3" height="1.3"/><rect x="9.2" y="9.5" width="1.3" height="1.3"/><rect x="5.5" y="11.8" width="1.3" height="1.3"/><rect x="7.4" y="11.8" width="1.3" height="1.3"/><rect x="9.2" y="11.8" width="1.3" height="1.3"/></g></svg>
        +966 (5)00387251
      </li>
      <li>
        <svg viewBox="0 0 16 16" aria-hidden="true"><rect x="4" y="1" width="8" height="5" fill="none" stroke-width="1.3"/><rect stroke="none" x="1" y="6" width="14" height="6" rx="1"/><rect x="4" y="10" width="8" height="5" fill="#fff" stroke-width="1.3"/><line x1="5.5" y1="12.5" x2="10.5" y2="12.5" stroke-width="1"/></svg>
        +966 (3)8842617
      </li>
      <li>
        <svg viewBox="0 0 16 16" aria-hidden="true"><rect x="1" y="3.5" width="14" height="9" fill="none" stroke-width="1.5"/><path d="M1.5 4l6.5 5 6.5-5M1.5 12l5-4.2M14.5 12l-5-4.2" fill="none" stroke-width="1.3"/></svg>
        tariq@qrv-example.com.sa
      </li>
      <li>
        <svg viewBox="0 0 16 16" aria-hidden="true"><circle cx="8" cy="8" r="7" stroke="none"/><path d="M4 4.5c1.5 0 2 1 3 1s1 1.5 0 2-2 0-2.5 1.5S6 12 5 12.5M10 3c0 1.5 1 2 2 2M11 9c1 0 1.5 1 1 2.5" fill="none" stroke="#fff" stroke-width="1.2"/></svg>
        www.qrv-example.com.sa
      </li>
    </ul>
  </section>

</div>
</body>
</html>
```